Boring Fiberglass Repair Company needs creative business cards

The Fiberglass Repair industry isn't very fun or creative but we'd like a business card that communicates a fresh, modern, and service-oriented feel. We repair bathroom fixtures (bath tubs, showers, etc) which are made out of fiberglass. Our fiberglass repair service will be sold to bathtub manufacturers and also businesses that sell bathtubs. We will also offer our services to home owners that have broken showers and bathtubs.
Target Market(s)
Home builders, plumbing wholesalers, home owners
Contact Information for Business Card
Name
Phone Number
Email Address
Business Address
Tag line: "Quality Craftsmanship Today"
Look and feel

```html
<!DOCTYPE html>
<html lang="en">
<head>
<meta charset="utf-8">
<title>Mesa Ridge Fiberglass – Business Card</title>
<link rel="stylesheet" href="https://fonts.googleapis.com/css2?family=Poppins:wght@400;500;700;800&display=swap">
<style>
  :root {
    --brand-red: #e3202b;
    --brand-navy: #1f2f66;
    --card-white: #ffffff;
    --stage: #1c1d21;
    --ink-navy: #22306b;
    --ink-dark: #2a2a2e;
  }
  * { margin: 0; padding: 0; box-sizing: border-box; }
  html, body {
    width: 1200px; height: 800px; overflow: hidden;
    background: var(--stage);
    font-family: "Poppins", sans-serif;
  }
  .canvas { position: relative; width: 1200px; height: 800px; }

  .card {
    position: absolute;
    width: 560px; height: 320px;
    border-radius: 2px;
    overflow: hidden;
    box-shadow: 0 18px 40px rgba(0,0,0,.45);
  }

  /* Front */
  .card-front {
    left: 90px; top: 70px;
    background: linear-gradient(150deg, var(--brand-red) 0%, var(--brand-red) 22%, #7a3354 52%, var(--brand-navy) 78%, var(--brand-navy) 100%);
    color: var(--card-white);
    display: flex; flex-direction: column; align-items: center; justify-content: center;
  }
  .wordmark { text-align: center; font-weight: 700; line-height: 1; }
  .wordmark-name { font-size: 46px; letter-spacing: 1px; }
  .wordmark-sub { font-size: 15px; letter-spacing: 15px; margin-top: 8px; padding-left: 15px; }
  .tagline { font-size: 14px; font-weight: 400; margin-top: 22px; letter-spacing: .3px; }

  /* Back */
  .card-back { left: 550px; top: 410px; background: var(--card-white); }
  .frame { position: absolute; inset: 0; width: 100%; height: 100%; }
  .back-panel {
    position: absolute; left: 22px; top: 20px; right: 22px; bottom: 24px;
    background: var(--card-white);
    display: flex; align-items: center; justify-content: center;
    padding-bottom: 34px;
  }
  .identity { text-align: right; padding-right: 16px; }
  .person-name { font-size: 18px; font-weight: 800; letter-spacing: -.3px; line-height: 1.05; }
  .person-name .first { color: var(--brand-red); }
  .person-name .last { color: var(--ink-navy); }
  .person-role { font-size: 14px; font-weight: 400; color: var(--ink-dark); line-height: 1.1; }
  .divider { width: 1.5px; height: 74px; background: var(--ink-navy); }
  .contact-list { list-style: none; padding-left: 16px; }
  .contact-list li {
    display: flex; align-items: center; gap: 8px;
    font-size: 13px; color: var(--ink-dark); line-height: 1.55;
  }
  .contact-list svg { width: 13px; height: 13px; flex: none; }
</style>
</head>
<body>
<main class="canvas">

  <section class="card card-front" aria-label="Card front">
    <div class="wordmark">
      <div class="wordmark-name">MESA RIDGE</div>
      <div class="wordmark-sub">FIBERGLASS</div>
    </div>
    <p class="tagline">Quality Craftsmanship Today</p>
  </section>

  <section class="card card-back" aria-label="Card back">
    <svg class="frame" viewBox="0 0 560 320" preserveAspectRatio="none" aria-hidden="true">
      <polygon points="0,0 560,0 560,320 470,320 150,0" fill="var(--brand-navy)"/>
      <polygon points="0,0 150,0 470,320 0,320" fill="var(--brand-red)"/>
    </svg>
    <div class="back-panel">
      <div class="identity">
        <div class="person-name"><span class="first">DANA</span> <span class="last">REYES</span></div>
        <div class="person-role">CEO</div>
      </div>
      <div class="divider"></div>
      <ul class="contact-list">
        <li>
          <svg viewBox="0 0 14 14" aria-hidden="true"><rect x="3" y="1" width="8" height="12" rx="1.5" fill="none" stroke="var(--brand-red)" stroke-width="1.6"/></svg>
          555 555 5555
        </li>
        <li>
          <svg viewBox="0 0 14 14" aria-hidden="true"><rect x="1" y="3" width="12" height="8" fill="var(--brand-red)"/><path d="M1 3 L7 8 L13 3" fill="none" stroke="#fff" stroke-width="1.2"/></svg>
          info@companygmail.com
        </li>
        <li>
          <svg viewBox="0 0 14 14" aria-hidden="true"><circle cx="7" cy="7" r="6" fill="var(--brand-red)"/><path d="M1 7 H13 M7 1 V13 M7 1 C3.5 4 3.5 10 7 13 M7 1 C10.5 4 10.5 10 7 13" fill="none" stroke="#fff" stroke-width=".8"/></svg>
          www.companywebsite.com
        </li>
      </ul>
    </div>
  </section>

</main>
</body>
</html>
```